Tessavale Communications

I need a very clean, uncomplicated design for an LA-based, very senior level strategic communications firm with about four associates. Landing page should stress LA, maybe a slider with downtown skyline, Malibu pier, and Rodeo Drive. In addition to landing page with firm's description, all else we'd need is services offered page and another for bios of associates.

Industry/Entity Type

Communications

Font styles to use
Sans Serif

```html
<!DOCTYPE html>
<html lang="en">
<head>
<meta charset="utf-8">
<title>Tessavale Communications</title>
<link rel="stylesheet" href="https://fonts.googleapis.com/css2?family=Roboto:wght@400;500;700&family=Open+Sans:ital,wght@0,400;0,600;0,700;1,400&display=swap">
<style>
:root{
  --blue:#2480d4;
  --blue-dark:#1c6fbd;
  --ink:#2b2b2b;
  --text:#3a3a3a;
  --muted:#7a7a7a;
  --topbar:#333333;
  --footer:#333333;
  --panel:#8fb7dc;
  --band:#dcdcdc;
  --line:#cfcfcf;
  --white:#ffffff;
}
*{box-sizing:border-box;margin:0;padding:0}
html,body{width:974px;height:1200px;overflow:hidden;background:var(--white)}
body{position:relative;font-family:"Open Sans",Arial,sans-serif;color:var(--text)}
.abs{position:absolute}
svg{display:block}

/* top bar */
.topbar{left:0;top:0;width:974px;height:22px;background:var(--topbar);color:#e6e6e6;font-size:10.5px}
.topbar .contact{left:142px;top:4px;display:flex;gap:22px}
.topbar .contact span{display:flex;align-items:center;gap:5px}
.topbar .account{right:139px;top:4px}

/* header */
.logo{left:140px;top:32px;display:flex;align-items:center;gap:8px}
.logo-mark{width:56px;height:56px;border-radius:50%;background:var(--blue)}
.logo-name{font-family:"Roboto",sans-serif;font-weight:700;font-size:23px;line-height:1.05;color:var(--blue)}
.nav{top:22px;left:448px;height:61px;display:flex;font-family:"Roboto",sans-serif;font-size:12px;color:var(--ink)}
.nav a{color:inherit;text-decoration:none;display:flex;align-items:center;justify-content:center;padding-top:0}
.nav .active{width:50px;background:var(--blue);color:var(--white);box-shadow:inset 0 3px 0 var(--blue-dark)}
.nav .item{margin-left:0}

/* hero */
.hero{left:0;top:98px;width:974px;height:320px;background:linear-gradient(180deg,#8db8df 0%,#a9c6dc 45%,#a9a39a 75%,#c9c2b6 100%)}
.hero-title{font-family:"Roboto",sans-serif;color:var(--white)}
.hero-title .line1{left:140px;top:185px;width:351px;height:42px;background:var(--blue);font-weight:700;font-size:31px;padding:3px 0 0 9px}
.hero-title .line2{left:140px;top:232px;width:306px;height:36px;background:var(--blue);font-size:31px;padding:0 0 0 7px;line-height:36px}
.hero-cta{left:140px;top:273px;width:258px;height:33px;background:#111;border:1px solid #555;border-radius:2px;color:var(--white);font-family:"Roboto",sans-serif;font-weight:500;font-size:16.5px;line-height:31px;padding-left:10px}
.hero-dots{left:141px;top:310px;display:flex;gap:4px}
.hero-dots i{width:8px;height:8px;border-radius:50%;background:#ddd}
.hero-dots i.on{background:var(--blue)}
.hero-arrow{top:243px;width:32px;height:32px;border-radius:50%;background:rgba(255,255,255,.6)}

/* welcome */
.welcome-title{left:140px;top:442px;font-family:"Roboto",sans-serif;font-weight:700;font-size:20px;color:var(--ink)}
.welcome-photo{left:140px;top:479px;width:156px;height:157px;background:linear-gradient(160deg,#10161f 0%,#1e3550 55%,#3fb0e6 100%)}
.welcome-text{left:311px;top:485px;width:276px;font-size:10px;line-height:13.4px}
.welcome-text p+p{margin-top:13px}
.welcome-more{left:141px;top:642px;width:445px;font-size:10px;line-height:13.4px}
.btn{border:1px solid var(--blue);border-radius:3px;background:var(--white);color:var(--blue-dark);font-weight:700;font-size:9.5px;display:flex;align-items:center;justify-content:center;gap:5px}
.view-more{left:511px;top:668px;width:74px;height:24px}

/* form */
.form-head{left:628px;top:442px;width:209px;height:31px;background:var(--blue);color:var(--white);font-weight:700;font-size:13px;text-align:center;line-height:30px;padding-left:18px;clip-path:polygon(0 0,100% 0,100% 100%,0 100%,14px 50%)}
.form-body{left:645px;top:473px;width:191px;height:223px;background:var(--panel)}
.field{left:653px;width:175px;height:25px;background:var(--white);border-radius:2px;font-size:9.5px;color:#999;padding:6px 9px;display:flex;justify-content:space-between}
.field.message{height:78px}
.submit{left:767px;top:662px;width:62px;height:24px;background:var(--blue);border:1px solid #5b9ad6;border-radius:3px;color:var(--white);font-weight:700;font-size:9.5px;display:flex;align-items:center;justify-content:center;gap:4px}

/* partners */
.partners-band{left:0;top:731px;width:974px;height:122px;background:var(--band)}
.partners-label{left:140px;top:717px;width:133px;height:26px;background:var(--band);font-family:"Roboto",sans-serif;font-weight:700;font-size:17px;color:var(--ink);padding:3px 0 0 4px}
.partner-arrow{top:780px;width:24px;height:24px;background:var(--blue)}
.partner{top:759px;width:106px;height:67px;border:1px solid #b9b9b9;background:#e1e1e1;display:flex;align-items:center;justify-content:center}
.partner i{display:block;width:62px;height:18px;background:#9a9a9a}
.partner i.sq{width:34px;height:34px}

/* testimonials */
.section-title{top:884px;font-family:"Roboto",sans-serif;font-weight:700;font-size:17px;color:var(--ink)}
.quote{left:141px;top:919px;width:360px;height:153px}
.quote-title{left:159px;top:932px;font-weight:600;font-size:10px;color:#1c2b44}
.quote-text{left:159px;top:950px;width:300px;font-style:italic;font-size:10px;line-height:13.4px;color:var(--muted)}
.quote-text p+p{margin-top:13px}
.client-photo{left:504px;top:919px;width:74px;height:73px;background:linear-gradient(180deg,#e8e4df 0%,#c9a27f 100%)}
.client-name{left:504px;top:995px;width:74px;text-align:center;font-size:10px}
.client-dots{left:548px;top:1021px;display:flex;gap:2px}
.client-dots i{width:7px;height:7px;border-radius:50%;background:#d4d4d4}
.client-dots i.on{background:var(--blue)}
.view-all{left:516px;top:1047px;width:67px;height:25px}

/* services */
.services{left:630px;top:915px;list-style:none;font-size:10px}
.services li{display:flex;align-items:center;gap:5px;height:20.4px}
.services span{border-bottom:1px solid #555;line-height:12px}
.services b{color:var(--blue);font-size:10px}

/* footer */
.footer-rule{left:0;top:1118px;width:974px;height:3px;background:var(--blue)}
.footer{left:0;top:1124px;width:974px;height:76px;background:var(--footer)}
.social{left:431px;top:1138px;display:flex;gap:9px}
.social i{width:20px;height:20px;border-radius:50%;background:#d9e3ee}
.copyright{left:0;top:1166px;width:974px;text-align:center;color:#eee;font-size:10px}
</style>
</head>
<body>

<div class="abs topbar">
  <div class="abs contact">
    <span><svg width="9" height="9" viewBox="0 0 10 10"><path d="M2 0.5l2 2-1 1.2c.6 1.3 1.5 2.2 2.8 2.8l1.2-1 2 2-1.3 1.6C4 8.6 1.3 6 .4 1.8z" fill="#ddd"/></svg>+0800 555 0142</span>
    <span><svg width="11" height="8" viewBox="0 0 11 8"><rect x=".5" y=".5" width="10" height="7" fill="none" stroke="#ddd"/><path d="M.5.5l5 4 5-4" fill="none" stroke="#ddd"/></svg>info@tessavale.com</span>
  </div>
  <div class="abs account">Login &nbsp;|&nbsp; Register</div>
</div>

<div class="abs logo">
  <div class="logo-mark"></div>
  <div class="logo-name">Tessavale<br>Communications</div>
</div>

<nav class="abs nav">
  <a class="active" href="#">Home</a>
  <a class="item" href="#" style="width:115px">About us</a>
  <a class="item" href="#" style="width:60px">Services</a>
  <a class="item" href="#" style="width:91px">Blog</a>
  <a class="item" href="#" style="width:78px">Contact Us</a>
</nav>

<div class="abs hero" role="img" aria-label="Downtown Los Angeles skyline with mountains behind, a man shouting into a megaphone on the right"></div>
<div class="hero-title">
  <div class="abs line1">ADVANCE THE EXTENT</div>
  <div class="abs line2">of communication</div>
</div>
<div class="abs hero-cta">CLICK HERE FOR MORE DETAIL</div>
<div class="abs hero-dots"><i class="on"></i><i></i><i></i></div>
<div class="abs hero-arrow" style="left:21px"><svg width="32" height="32"><path d="M19 10l-6 6 6 6" stroke="#444" fill="none" stroke-width="1.3"/></svg></div>
<div class="abs hero-arrow" style="left:921px"><svg width="32" height="32"><path d="M13 10l6 6-6 6" stroke="#444" fill="none" stroke-width="1.3"/></svg></div>

<h1 class="abs welcome-title">Welcome to Tessavale Communication</h1>
<div class="abs welcome-photo" role="img" aria-label="Businessman in a suit touching a glowing tablet with floating app icons"></div>
<div class="abs welcome-text">
  <p>Nunc malesuada mauris quis neque egestas ullamcorper at quis magna. Sed eget turpis ipsum. Etiam eget augue ut turpis semper volutpat ut non dolor. Maecenas a nibh ac elit faucibus vestibulum ut quis sem. Duis dictum justo non eleifend consequat. Curabitur a malesuada turpis. Nam vitae convallis dolor, ut malesuada neque. Curabitur blandit posuere aliquam. Sed porttitor ultricies iaculis. Ut dapibus rutrum lectus.</p>
  <p>Ut mattis a est eget luctus. Nulla interdum metus vitae turpis rhoncus, id porta nibh bibendum. Maecenas consequat malesuada arcu sed consectetur.</p>
</div>
<p class="abs welcome-more">Donec condimentum tristique augue, vel venenatis lectus placerat sit amet. Phasellus efficitur justo eu placerat sagittis.</p>
<a class="abs btn view-more">View more <svg width="9" height="9"><circle cx="4.5" cy="4.5" r="4.5" fill="#1c6fbd"/><path d="M3.5 2.5l2 2-2 2" stroke="#fff" fill="none"/></svg></a>

<div class="abs form-head">Get Started Today</div>
<div class="abs form-body"></div>
<div class="abs field" style="top:491px"><span>Name*</span><svg width="8" height="9"><circle cx="4" cy="2.5" r="2.3" fill="#999"/><path d="M0 9c0-3 1.8-4.3 4-4.3S8 6 8 9z" fill="#999"/></svg></div>
<div class="abs field" style="top:520px"><span>Email</span><svg width="10" height="8"><rect width="10" height="8" fill="#999"/><path d="M0 0l5 4 5-4" stroke="#fff" fill="none"/></svg></div>
<div class="abs field" style="top:548px"><span>Phone number</span><svg width="8" height="8" viewBox="0 0 10 10"><path d="M2 .5l2 2-1 1.2c.6 1.3 1.5 2.2 2.8 2.8l1.2-1 2 2-1.3 1.6C4 8.6 1.3 6 .4 1.8z" fill="#999"/></svg></div>
<div class="abs field message" style="top:577px"><span>Message</span><svg width="10" height="8"><ellipse cx="5" cy="3.5" rx="5" ry="3.5" fill="#999"/></svg></div>
<div class="abs submit">Submit <svg width="9" height="9"><circle cx="4.5" cy="4.5" r="4.5" fill="#fff"/><path d="M3.5 2.5l2 2-2 2" stroke="#2480d4" fill="none"/></svg></div>

<div class="abs partners-band" role="img" aria-label="Faint pattern of communication device icons"></div>
<h2 class="abs partners-label">OUR PARTNERS</h2>
<div class="abs partner-arrow" style="left:140px"><svg width="24" height="24"><path d="M14 7l-5 5 5 5" stroke="#fff" fill="none" stroke-width="1.6"/></svg></div>
<div class="abs partner-arrow" style="left:812px"><svg width="24" height="24"><path d="M10 7l5 5-5 5" stroke="#fff" fill="none" stroke-width="1.6"/></svg></div>
<div class="abs partner" style="left:184px"><i class="sq"></i></div>
<div class="abs partner" style="left:309px"><i></i></div>
<div class="abs partner" style="left:434px"><i></i></div>
<div class="abs partner" style="left:560px"><i></i></div>
<div class="abs partner" style="left:685px"><i></i></div>

<h2 class="abs section-title" style="left:142px">WHAT CLIENT SAYS ABOUT US</h2>
<svg class="abs quote" viewBox="0 0 360 153"><path d="M.5 .5H359.5L338 20V152.5H.5Z" fill="#fff" stroke="#cfcfcf"/></svg>
<div class="abs quote-title">Aliquam adipiscing vulputate turpis</div>
<div class="abs quote-text">
  <p>Duis purus odio, scelerisque nec lectus tinci dunt, hendrerit ultrices augue. Nulla adipis cing ante in arcu vehicula ultrices. Aliquam erat volutpat.</p>
  <p>Proin porttitor justo vitae arcu dapibus feugiat. Fusce et sapien tortor. Fusce interdum Donec scelerisque nibh nec vestibulum tristique. Donec ligula massa, eleifend sed luctus nec, dictum eu augue.</p>
</div>
<div class="abs client-photo" role="img" aria-label="Portrait of a smiling client"></div>
<div class="abs client-name">Fusce Eleifend</div>
<div class="abs client-dots"><i></i><i></i><i class="on"></i></div>
<a class="abs btn view-all">View all <svg width="9" height="9"><circle cx="4.5" cy="4.5" r="4.5" fill="#1c6fbd"/><path d="M3.5 2.5l2 2-2 2" stroke="#fff" fill="none"/></svg></a>

<h2 class="abs section-title" style="left:630px">OUR SERVICES</h2>
<ul class="abs services">
  <li><b>›</b><span>Vivamus posuere tempus eros eget</span></li>
  <li><b>›</b><span>Vivamus pulvinar ac velit at molestie.</span></li>
  <li><b>›</b><span>Proin ut aliquet diam. Etiam ex mi ultrices</span></li>
  <li><b>›</b><span>Eget nisl vitae, iaculis consectetur diam.</span></li>
  <li><b>›</b><span>Donec condimentum ex vel neque vehicula</span></li>
  <li><b>›</b><span>Proin interdum vehicula eleifend</span></li>
  <li><b>›</b><span>Proin posuere pretium odio, vitae mollis</span></li>
  <li><b>›</b><span>Cras venenatis justo sed ex commodo</span></li>
</ul>

<div class="abs footer-rule"></div>
<footer class="abs footer"></footer>
<div class="abs social"><i></i><i></i><i></i><i></i></div>
<div class="abs copyright">Copyright © 2014, all rights reserved.</div>

</body>
</html>
```